Engineering and Energy service provider

We need a design that gives the impression of a high level of technical competence and a reliable partner. Simple structure with little need for updates.
The company brand is Volnar and today consists of two main businesses: energy optimisation (Volnar energy) and technical consultancy (Volnar Engineering). Volnar energy is shown in the attached powerpoint,
We are a young growing company that consists of several businesses, the largest parts are energy monitoring services and consulting services. Consulting services for commercial installations in the technical area of cooling, ventilation, heating and energy. Services offered include project planning, project management, inspection, operational analysis and technical investigations. Energy monitoring and optimization services are performed as a subscription with a subscription to the service.
Target Market(s)
Commercial property owners Grocery retail, grocery stores, construction companies
Industry/Entity Type
energy services and consulting services
Coding
Coded - Design and coding required
Number of Pages Required
5+ page
Look and feel
Each slider illustrates characteristics of the customer's brand and the style your logo design should communicate.

```html
<!DOCTYPE html>
<html lang="en">
<head>
<meta charset="utf-8">
<title>Volnar Engineering</title>
<link href="https://fonts.googleapis.com/css2?family=Exo+2:wght@500;600;700;800&family=Open+Sans:wght@400;600;700&display=swap" rel="stylesheet">
<style>
:root{
  --blue-deep:#0b2f86;
  --blue:#1553c7;
  --blue-bright:#1f74e8;
  --blue-light:#4a9cf5;
  --ink:#0f1c3a;
  --text:#4a5570;
  --white:#ffffff;
  --dark:#0a1226;
  --line:rgba(255,255,255,.25);
}
*{box-sizing:border-box;margin:0;padding:0}
html,body{width:1200px;height:2680px;overflow:hidden}
body{font-family:"Open Sans",Arial,sans-serif;color:var(--text);background:var(--white);position:relative}
h1,h2,h3,.display{font-family:"Exo 2","Open Sans",sans-serif}
.btn{display:inline-block;font-family:"Exo 2",sans-serif;font-weight:600;font-size:13px;padding:11px 22px;border-radius:3px;text-decoration:none}
.btn-light{background:var(--white);color:var(--blue)}
.btn-outline{border:1px solid var(--white);color:var(--white)}
.btn-blue{background:var(--blue);color:var(--white)}

/* hero */
.hero{position:relative;height:470px;background:linear-gradient(120deg,var(--blue-deep) 0%,var(--blue) 55%,var(--blue-bright) 100%);color:var(--white);overflow:hidden}
.hero-photo{position:absolute;inset:0;background:linear-gradient(100deg,rgba(10,40,120,0) 0%,rgba(60,140,240,.35) 60%,rgba(20,70,180,.2) 100%)}
.nav{position:relative;display:flex;align-items:center;justify-content:space-between;padding:0 80px;height:56px}
.brand{font-family:"Exo 2",sans-serif;font-weight:800;font-size:26px;letter-spacing:2px;color:var(--white);display:flex;align-items:center;gap:10px}
.brand .mark{width:12px;height:12px;background:var(--white)}
.nav ul{list-style:none;display:flex;gap:30px;align-items:center;font-family:"Exo 2",sans-serif;font-weight:600;font-size:12px;letter-spacing:.5px;text-transform:uppercase}
.nav li.active{border-bottom:2px solid var(--white);padding-bottom:4px}
.nav li.cta{background:var(--blue-bright);padding:7px 14px;border-radius:2px}
.hero-copy{position:absolute;left:80px;top:100px;width:560px}
.eyebrow{font-size:12px;font-weight:600;letter-spacing:1px;opacity:.85;margin-bottom:10px}
.hero-copy h1{font-size:36px;line-height:1.18;font-weight:700;margin-bottom:14px}
.hero-copy p{font-size:14px;line-height:1.6;opacity:.9;margin-bottom:22px}
.hero-copy .btn{margin-right:10px}
.hero-device{position:absolute;left:760px;top:70px;width:330px;height:320px;border-radius:22px;background:linear-gradient(150deg,#e9eef7,#b9c8e4);transform:rotate(-6deg);box-shadow:0 18px 40px rgba(0,0,30,.35)}
.hero-edge{position:absolute;left:0;bottom:0;width:1200px;height:60px}

/* stats */
.stats{position:relative;height:230px;background:var(--blue)}
.stats-row{position:absolute;left:100px;top:0;width:1000px;display:grid;grid-template-columns:repeat(4,1fr);gap:16px}
.stat{height:140px;border:1px solid var(--line);background:rgba(255,255,255,.06);color:var(--white);text-align:center;padding-top:18px}
.stat .icon{width:46px;height:46px;margin:0 auto 10px;border-radius:50%;border:2px solid rgba(255,255,255,.8);display:flex;align-items:center;justify-content:center}
.stat strong{display:block;font-family:"Exo 2",sans-serif;font-size:24px;font-weight:700}
.stat span{font-size:12px;opacity:.85}
.stat.featured{background:var(--white);color:var(--blue);border-color:var(--white);transform:translateY(-12px);height:164px;padding-top:28px;box-shadow:0 12px 28px rgba(0,0,40,.25)}
.stat.featured .icon{border-color:var(--blue)}
.stats-edge{position:absolute;left:0;bottom:0;width:1200px;height:70px}

/* intro */
.intro{position:relative;height:400px;overflow:hidden}
.section-label{text-align:center;font-size:10px;font-weight:700;letter-spacing:2px;color:var(--blue-bright);text-transform:uppercase}
.section-title{text-align:center;font-size:28px;font-weight:700;color:var(--ink);margin-top:4px}
.intro .section-label{padding-top:26px}
.watermark{position:absolute;right:40px;top:250px;font-family:"Exo 2",sans-serif;font-weight:800;font-size:60px;letter-spacing:10px;color:rgba(21,83,199,.05);z-index:0}
.intro-media{position:absolute;left:100px;top:110px;width:490px;height:230px;background:linear-gradient(120deg,#0d2a66,#2d6fd6 70%,#8db8f0);clip-path:polygon(8% 0,100% 0,92% 100%,0 100%)}
.intro-badge{position:absolute;left:430px;top:290px;width:160px;padding:10px 14px;background:var(--blue-deep);color:var(--white);font-family:"Exo 2",sans-serif;font-weight:700;font-size:14px;line-height:1.2;text-transform:uppercase;text-align:center}
.intro-text{position:absolute;left:630px;top:120px;width:470px;z-index:1}
.intro-text h3{font-size:18px;color:var(--blue);font-weight:700;margin-bottom:8px}
.intro-text p{font-size:12.5px;line-height:1.6;margin-bottom:10px}
.ticks{list-style:none;font-size:12.5px;line-height:1.8;margin-bottom:12px}
.ticks li{display:flex;align-items:center;gap:8px}
.ticks svg{flex:none}

/* services */
.services{position:relative;height:520px;background:linear-gradient(180deg,var(--blue) 0%,var(--blue-deep) 100%);color:var(--white)}
.services .section-title{color:var(--white);padding-top:40px}
.service-grid{position:absolute;left:150px;top:120px;width:900px;display:grid;grid-template-columns:repeat(3,1fr);gap:20px}
.service-photo{height:170px}
.service-photo.monitor{background:linear-gradient(140deg,#1c3a7a,#5c8fd8)}
.service-photo.consult{background:linear-gradient(140deg,#c9d6e8,#6e8fbf)}
.service-photo.inspect{background:linear-gradient(140deg,#e4e8ef,#8ea4c6)}
.service-body{background:var(--blue-bright);padding:16px 18px;height:170px}
.service-body h3{font-size:16px;font-weight:700;margin-bottom:8px}
.service-body p{font-size:11.5px;line-height:1.6;opacity:.92;margin-bottom:12px}
.service-body .btn{font-size:10px;padding:6px 12px}
.service:nth-child(2) .service-body{background:var(--blue-light)}

/* management */
.management{position:relative;height:460px}
.management .section-title{padding-top:44px;font-size:30px}
.mgmt-text{position:absolute;left:100px;top:140px;width:480px}
.mgmt-text h3{font-size:17px;font-weight:700;color:var(--ink);margin-bottom:8px}
.mgmt-text p{font-size:12.5px;line-height:1.6;margin-bottom:10px}
.mgmt-media{position:absolute;left:630px;top:130px;width:470px;height:250px;background:linear-gradient(130deg,#0a1a44,#26508f 60%,#6d8fc4);clip-path:polygon(10% 0,100% 0,90% 100%,0 100%)}
.mgmt-badge{position:absolute;left:700px;top:340px;width:180px;padding:10px 14px;background:var(--blue);color:var(--white);font-family:"Exo 2",sans-serif;font-weight:700;font-size:14px;line-height:1.2;text-transform:uppercase;text-align:center}

/* closing backdrop with footer */
.closing{position:relative;height:600px;background:linear-gradient(180deg,#2a3d66 0%,#1a2a4c 35%,#101b34 65%,var(--dark) 100%);color:#b7c1d6}
.closing-photo{position:absolute;left:0;right:0;top:0;height:330px;background:linear-gradient(90deg,rgba(74,156,245,.18),rgba(20,40,90,.05) 50%,rgba(74,156,245,.15))}
.closing-edge{position:absolute;left:0;top:0;width:1200px;height:110px}
.footer{position:absolute;left:100px;right:100px;top:300px;display:grid;grid-template-columns:1.6fr 1fr 1fr 1.2fr;gap:40px}
.footer .brand{font-size:24px;margin-bottom:12px}
.footer p{font-size:11.5px;line-height:1.6}
.footer h4{font-family:"Exo 2",sans-serif;color:var(--white);font-size:13px;font-weight:700;margin-bottom:10px}
.footer ul{list-style:none;font-size:11.5px;line-height:1.9}
.footer .btn{margin-top:10px;font-size:11px;padding:8px 14px}
.copyright{position:absolute;left:100px;right:100px;bottom:34px;padding-top:16px;border-top:1px solid rgba(255,255,255,.1);font-size:10.5px;color:#6f7b94}
</style>
</head>
<body>

<header class="hero">
  <div class="hero-photo" role="img" aria-label="Server room with blue-lit equipment racks"></div>
  <nav class="nav">
    <div class="brand"><span class="mark"></span>VOLNAR</div>
    <ul>
      <li class="active">Home</li>
      <li>Energy monitoring</li>
      <li>Consulting</li>
      <li>Projects</li>
      <li>About</li>
      <li class="cta">Contact</li>
    </ul>
  </nav>
  <div class="hero-copy">
    <div class="eyebrow">Energy · HVAC · Consulting</div>
    <h1>Reliable engineering partner for energy monitoring &amp; building systems</h1>
    <p>We help commercial property owners and grocery retailers cut energy use and improve system performance. From subscription monitoring to project management, inspections and technical reviews.</p>
    <a class="btn btn-light" href="#">See monitoring plans</a>
    <a class="btn btn-outline" href="#">Talk to an engineer</a>
  </div>
  <div class="hero-device" role="img" aria-label="Tablet showing an energy monitoring dashboard with charts and gauges"></div>
  <svg class="hero-edge" viewBox="0 0 1200 60" preserveAspectRatio="none" aria-hidden="true">
    <polygon points="0,60 1200,20 1200,60" fill="#1553c7"/>
  </svg>
</header>

<section class="stats">
  <div class="stats-row">
    <div class="stat">
      <div class="icon"><svg width="22" height="22" viewBox="0 0 24 24" fill="none" stroke="#fff" stroke-width="2"><circle cx="12" cy="12" r="9"/><path d="M12 7v5l3 2"/></svg></div>
      <strong>24/7</strong><span>Monitoring</span>
    </div>
    <div class="stat featured">
      <div class="icon"><svg width="22" height="22" viewBox="0 0 24 24" fill="none" stroke="#1553c7" stroke-width="2"><path d="M4 18l5-6 4 3 7-9"/></svg></div>
      <strong>15–25%</strong><span>Typical savings</span>
    </div>
    <div class="stat">
      <div class="icon"><svg width="22" height="22" viewBox="0 0 24 24" fill="none" stroke="#fff" stroke-width="2"><circle cx="12" cy="12" r="2"/><path d="M12 10V4M14 12h6M12 14v6M10 12H4"/></svg></div>
      <strong>HVAC</strong><span>Cooling · Ventilation · Heating</span>
    </div>
    <div class="stat">
      <div class="icon"><svg width="22" height="22" viewBox="0 0 24 24" fill="none" stroke="#fff" stroke-width="2"><path d="M12 3l8 3v6c0 5-4 8-8 9-4-1-8-4-8-9V6z"/><path d="M8.5 12l2.5 2.5 4.5-5"/></svg></div>
      <strong>SLA</strong><span>Clear response windows</span>
    </div>
  </div>
  <svg class="stats-edge" viewBox="0 0 1200 70" preserveAspectRatio="none" aria-hidden="true">
    <polygon points="0,70 600,0 1200,70" fill="#ffffff"/>
  </svg>
</section>

<section class="intro">
  <div class="section-label">Welcome</div>
  <h2 class="section-title">Volnar Engineering</h2>
  <div class="watermark display">ENGINEERING</div>
  <div class="intro-media" role="img" aria-label="Hand touching a glowing digital security and energy interface"></div>
  <div class="intro-badge">Plan an energy scan</div>
  <div class="intro-text">
    <h3>Designed for grocery retail &amp; commercial properties</h3>
    <p>Stores, construction partners and property owners rely on us to keep refrigeration, ventilation and heating efficient, safe and compliant year round.</p>
    <ul class="ticks">
      <li><svg width="12" height="12" viewBox="0 0 12 12"><path d="M2 6l3 3 5-6" fill="none" stroke="#1553c7" stroke-width="2"/></svg>Verified savings reporting</li>
      <li><svg width="12" height="12" viewBox="0 0 12 12"><path d="M2 6l3 3 5-6" fill="none" stroke="#1553c7" stroke-width="2"/></svg>Commissioning and retrofit planning</li>
      <li><svg width="12" height="12" viewBox="0 0 12 12"><path d="M2 6l3 3 5-6" fill="none" stroke="#1553c7" stroke-width="2"/></svg>Clear contacts and fast follow-up</li>
    </ul>
    <a class="btn btn-blue" href="#">Learn more</a>
  </div>
</section>

<section class="services">
  <h2 class="section-title">Volnar Engineering</h2>
  <div class="service-grid">
    <article class="service">
      <div class="service-photo monitor" role="img" aria-label="Control panel screen displaying energy data"></div>
      <div class="service-body">
        <h3>Energy Monitoring</h3>
        <p>Subscription monitoring that tracks consumption, flags deviations and turns data into action.</p>
        <a class="btn btn-light" href="#">Read more</a>
      </div>
    </article>
    <article class="service">
      <div class="service-photo consult" role="img" aria-label="Engineers in hard hats reviewing plans on site"></div>
      <div class="service-body">
        <h3>Technical Consulting</h3>
        <p>Project planning and management for cooling, ventilation, heating and energy installations.</p>
        <a class="btn btn-light" href="#">Read more</a>
      </div>
    </article>
    <article class="service">
      <div class="service-photo inspect" role="img" aria-label="Technician inspecting building documents at a desk"></div>
      <div class="service-body">
        <h3>Inspections &amp; Investigations</h3>
        <p>Operational analysis, inspections and technical investigations with clear, practical findings.</p>
        <a class="btn btn-light" href="#">Read more</a>
      </div>
    </article>
  </div>
</section>

<section class="management">
  <h2 class="section-title">Management that makes a difference</h2>
  <div class="mgmt-text">
    <h3>Subscription service that finds savings continuously</h3>
    <p>Our engineers follow your systems every month, compare usage with baselines and recommend adjustments before small faults become costly problems.</p>
    <ul class="ticks">
      <li><svg width="12" height="12" viewBox="0 0 12 12"><path d="M2 6l3 3 5-6" fill="none" stroke="#1553c7" stroke-width="2"/></svg>Fault detection with alerts and priorities</li>
      <li><svg width="12" height="12" viewBox="0 0 12 12"><path d="M2 6l3 3 5-6" fill="none" stroke="#1553c7" stroke-width="2"/></svg>Monthly reports with clear next steps</li>
      <li><svg width="12" height="12" viewBox="0 0 12 12"><path d="M2 6l3 3 5-6" fill="none" stroke="#1553c7" stroke-width="2"/></svg>Direct contact with your assigned engineer</li>
    </ul>
    <a class="btn btn-blue" href="#">Learn more</a>
  </div>
  <div class="mgmt-media" role="img" aria-label="Business hand pointing at rising digital bar chart"></div>
  <div class="mgmt-badge">All plans<br>reporting &amp; action</div>
</section>

<section class="closing">
  <div class="closing-photo" role="img" aria-label="Dark city skyline with commercial buildings at dusk"></div>
  <svg class="closing-edge" viewBox="0 0 1200 110" preserveAspectRatio="none" aria-hidden="true">
    <polygon points="0,0 1200,0 1200,10 0,110" fill="#ffffff"/>
  </svg>
  <footer class="footer">
    <div>
      <div class="brand"><span class="mark"></span>VOLNAR</div>
      <p>Energy monitoring and technical consulting for commercial properties, grocery retail and construction partners.</p>
    </div>
    <div>
      <h4>Services</h4>
      <ul><li>Energy monitoring</li><li>Project planning</li><li>Inspections</li><li>Operational analysis</li></ul>
    </div>
    <div>
      <h4>Company</h4>
      <ul><li>About</li><li>Projects</li><li>Careers</li><li>Contact</li></ul>
    </div>
    <div>
      <h4>Contact</h4>
      <ul><li>+00 100 200 300</li><li>hello@volnar.example</li><li>Harbour Street 12</li></ul>
      <a class="btn btn-blue" href="#">Book an energy scan</a>
    </div>
  </footer>
  <div class="copyright">© Volnar Engineering. All rights reserved.</div>
</section>

</body>
</html>
```